A slider bar and icons to be used on the map

#Background
We are currently creating a website for tourists to Japan . Named "Maple Trove," It's a website where users can search for shrines and temples across Japan on the map. We are seeking designs for three icons(shrine icon, temple icon, and representing both shrine and temple icon) and a slider bar to be used on this site's map.
#Requirements
Cool and understandable icons and a slider bar that match the web design.
#Web Design Concept
Attached is a reference document.
#Desired Items
We need four items written below.
-Shrine icon
-Temple icon
-Icon representing both shrines and temples (expressed as a single icon)
-Slider bar
#Regarding the Slider Bar
It has two functions:
-Filter popular shrines and temples.
-Filiter shrines and temples with cool kanji.
We would like it to be able to filter from both the right and the left.
We want to express that moving to the right represents popularity or cool kanji. We'd like to express this on the slider bar as a design.
* reference> https://snaps.vextoro.io/k4TnQw8zLp2HsVbX7
Updates
Need extra days to review
Target Market(s)
Inbound tourists to Japan
Look and feel

```html
<!DOCTYPE html>
<html lang="en">
<head>
<meta charset="utf-8">
<title>Maple Trove – Map Filter Sliders</title>
<link rel="stylesheet" href="https://fonts.googleapis.com/css2?family=Barlow:wght@400&display=swap">
<style>
  :root {
    --bg: #ffffff;
    --track: #d3d4d6;
    --track-edge: #b4b5b7;
    --knob: #ffffff;
    --knob-edge: #a9aaac;
    --label: #808184;
    --icon-green: #8dc63f;
    --icon-grey: #bcbec0;
    --fill-start: #fac712;
    --fill-mid: #f5a431;
    --fill-end: #ee6c3d;
  }
  html, body {
    margin: 0;
    padding: 0;
    width: 1200px;
    height: 1200px;
    overflow: hidden;
    background: var(--bg);
  }
  .slider-sheet { display: block; width: 1200px; height: 1200px; }
  .track { fill: var(--track); stroke: var(--track-edge); stroke-width: 0.6; }
  .range { fill: url(#range-gradient); }
  .knob { fill: var(--knob); stroke: var(--knob-edge); stroke-width: 0.6; }
  .label {
    font-family: "Barlow", "Helvetica Neue", Arial, sans-serif;
    font-size: 21px;
    letter-spacing: 0.4px;
    fill: var(--label);
  }
  .label--end { text-anchor: end; }
  .icon-slot { rx: 4px; }
  .icon-slot--active { fill: var(--icon-green); }
  .icon-slot--muted { fill: var(--icon-grey); }
</style>
</head>
<body>
<svg class="slider-sheet" viewBox="0 0 1200 1200" xmlns="http://www.w3.org/2000/svg">
  <defs>
    <linearGradient id="range-gradient" gradientUnits="userSpaceOnUse" x1="400" y1="0" x2="935" y2="0">
      <stop offset="0" stop-color="var(--fill-start)"/>
      <stop offset="0.5" stop-color="var(--fill-mid)"/>
      <stop offset="1" stop-color="var(--fill-end)"/>
    </linearGradient>
  </defs>

  <!-- Slider 1 -->
  <g class="slider">
    <rect class="track" x="122" y="264.5" width="951" height="25" rx="12.5"/>
    <rect class="range" x="482" y="264" width="179" height="24"/>
    <circle class="knob" cx="482" cy="277" r="21.5"/>
    <circle class="knob" cx="661" cy="273" r="21.5"/>
    <text class="label" x="127" y="320">Popularity</text>
    <text class="label label--end" x="1079" y="320">Stylish Kanji</text>
    <rect class="icon-slot icon-slot--muted" x="458" y="195" width="50" height="50" rx="4"
          role="img" aria-label="Grey temple icon marking the left handle"/>
    <rect class="icon-slot icon-slot--active" x="639" y="204" width="44" height="38" rx="4"
          role="img" aria-label="Green shrine gate icon marking the right handle"/>
  </g>

  <!-- Slider 2 -->
  <g class="slider">
    <rect class="track" x="122" y="503.5" width="951" height="25" rx="12.5"/>
    <rect class="range" x="386" y="503" width="374" height="24"/>
    <circle class="knob" cx="386" cy="516" r="21.5"/>
    <circle class="knob" cx="760" cy="512" r="21.5"/>
    <text class="label" x="127" y="559">Popularity</text>
    <text class="label label--end" x="1079" y="559">Stylish Kanji</text>
    <rect class="icon-slot icon-slot--active" x="735" y="433" width="50" height="46" rx="4"
          role="img" aria-label="Green small temple icon marking the right handle"/>
  </g>

  <!-- Slider 3 -->
  <g class="slider">
    <rect class="track" x="122" y="756.5" width="951" height="25" rx="12.5"/>
    <rect class="range" x="386" y="756" width="474" height="24"/>
    <circle class="knob" cx="386" cy="769" r="21.5"/>
    <circle class="knob" cx="860" cy="769" r="21.5"/>
    <text class="label" x="127" y="812">Popularity</text>
    <text class="label label--end" x="1079" y="812">Stylish Kanji</text>
    <rect class="icon-slot icon-slot--active" x="830" y="673" width="60" height="56" rx="4"
          role="img" aria-label="Green medium temple icon marking the right handle"/>
  </g>

  <!-- Slider 4 -->
  <g class="slider">
    <rect class="track" x="122" y="988.5" width="951" height="25" rx="12.5"/>
    <rect class="range" x="386" y="988" width="555" height="24"/>
    <circle class="knob" cx="386" cy="1001" r="21.5"/>
    <circle class="knob" cx="941" cy="997" r="21.5"/>
    <text class="label" x="127" y="1044">Popularity</text>
    <text class="label label--end" x="1079" y="1044">Stylish Kanji</text>
    <rect class="icon-slot icon-slot--active" x="910" y="904" width="62" height="57" rx="4"
          role="img" aria-label="Green large temple icon marking the right handle"/>
  </g>
</svg>
</body>
</html>
```